Business Card Design

Psychotherapy and Therapeutic Counselling

As well as Life Coaching.

Industry/Entity Type

Business

Contact Information for Business Card

Harbour
Life Coaching Services
Confidential and Compassionate
KT FdSc Qualified Practitioner

Tel 07481502637

```html
<!DOCTYPE html>
<html lang="en">
<head>
<meta charset="utf-8">
<title>Business Card</title>
<link rel="stylesheet" href="https://fonts.googleapis.com/css2?family=Jost:wght@600&family=Questrial&display=swap">
<style>
  :root {
    --card-bg: #ffffff;
    --ink: #1a1a1a;
    --feather-light: #f1f1f1;
    --feather-mid: #cfcfcf;
    --feather-dark: #b9b9b9;
  }
  html, body {
    margin: 0;
    padding: 0;
    width: 1200px;
    height: 791px;
    overflow: hidden;
    background: var(--card-bg);
  }
  .card {
    position: relative;
    width: 1200px;
    height: 791px;
    background: var(--card-bg);
    color: var(--ink);
    font-family: "Questrial", "Century Gothic", sans-serif;
    overflow: hidden;
  }
  .wing-art {
    position: absolute;
    left: 0;
    top: 0;
    width: 1200px;
    height: 791px;
  }
  .contact {
    position: absolute;
    left: 35px;
    top: 84px;
    margin: 0;
  }
  .contact__name {
    font-family: "Jost", "Century Gothic", sans-serif;
    font-weight: 600;
    font-size: 42px;
    line-height: 52px;
    margin: 0;
  }
  .contact__line {
    font-size: 34px;
    line-height: 47px;
    margin: 0;
  }
  .services {
    position: absolute;
    right: 33px;
    bottom: 36px;
    text-align: right;
  }
  .services__tagline {
    font-family: "Jost", "Century Gothic", sans-serif;
    font-weight: 600;
    font-size: 36px;
    line-height: 46px;
    margin: 0;
  }
  .services__list {
    font-size: 34px;
    line-height: 46px;
    margin: 0;
  }
</style>
</head>
<body>
  <div class="card">
    <svg class="wing-art" viewBox="0 0 1200 791" role="img" aria-label="Soft grey sweeping wing motif rising across the right side of the card">
      <defs>
        <radialGradient id="wingGlow" cx="880" cy="230" r="520" gradientUnits="userSpaceOnUse">
          <stop offset="0" stop-color="var(--feather-dark)" stop-opacity="0.75"/>
          <stop offset="0.45" stop-color="var(--feather-mid)" stop-opacity="0.5"/>
          <stop offset="0.8" stop-color="var(--feather-light)" stop-opacity="0.35"/>
          <stop offset="1" stop-color="var(--card-bg)" stop-opacity="0"/>
        </radialGradient>
      </defs>
      <rect x="470" y="0" width="730" height="791" fill="url(#wingGlow)"/>
    </svg>

    <div class="contact">
      <p class="contact__name">*Name Here*</p>
      <p class="contact__line">FdSc Qualified Practitioner</p>
      <p class="contact__line">t: 07481502637</p>
      <p class="contact__line">e: xxxx@xxxx.net</p>
    </div>

    <div class="services">
      <p class="services__tagline">Confidential and Compassionate</p>
      <p class="services__list">Psychotherapy . Therapeutic Counselling . Life Coaching</p>
    </div>
  </div>
</body>
</html>
```